Complete Banner Set For Web Display Ads - Including Zimbly

Ads are driving to a free web class on real estate investing made easy. The offer is for software and training that solves their number 1 challenge - Finding Deals.
Examples of copy suggestions and offer....
"Invest In Real Estate Like A Pro"
"Access Never Before Seen Inventory In Seconds"
"The Country's Best Source For Off-Market Deals"
Brody Halvaney "#1 Real Estate Investing Strategy"
Real Estate

```html
<!DOCTYPE html>
<html lang="en">
<head>
<meta charset="utf-8">
<title>Brody Halvaney – #1 Real Estate Investing Strategy</title>
<link rel="stylesheet" href="https://fonts.googleapis.com/css2?family=Arimo:wght@400;700&display=swap">
<style>
  :root {
    --orange-light: #fbb04a;
    --orange: #f7941d;
    --orange-deep: #f26f21;
    --green: #8dc63f;
    --green-dark: #5f9a1e;
    --white: #ffffff;
    --mist: #eceef0;
    --ink: #111111;
    --button-ink: #1d2a10;
    --arrow: #2f4a16;
    --portrait-top: #d7c2b2;
    --portrait-mid: #cfd1d3;
    --portrait-low: #dcdee0;
  }
  html, body {
    margin: 0;
    padding: 0;
    width: 1200px;
    height: 2400px;
    overflow: hidden;
    background: var(--white);
  }
  .banner {
    position: relative;
    width: 1200px;
    height: 2400px;
    overflow: hidden;
    font-family: "Arimo", Arial, sans-serif;
    color: var(--ink);
  }
  .banner__backdrop {
    position: absolute;
    inset: 0;
    width: 1200px;
    height: 2400px;
  }
  .banner__portrait {
    position: absolute;
    left: 620px;
    top: 330px;
    width: 580px;
    height: 2070px;
    border-radius: 240px 0 0 0;
    background: linear-gradient(180deg, var(--portrait-top) 0%, var(--portrait-mid) 40%, var(--portrait-low) 100%);
  }
  .banner__name {
    position: absolute;
    left: 76px;
    top: 176px;
    margin: 0;
    font-size: 100px;
    font-weight: 700;
    letter-spacing: -1px;
    line-height: 1;
    white-space: nowrap;
  }
  .banner__headline {
    position: absolute;
    left: 78px;
    top: 380px;
    margin: 0;
    font-weight: 400;
    font-size: 124px;
    line-height: 160px;
    letter-spacing: -2px;
  }
  .banner__rank {
    display: block;
    font-weight: 700;
    font-size: 112px;
  }
  .banner__cta {
    position: absolute;
    left: 192px;
    top: 2132px;
    width: 808px;
    height: 188px;
    box-sizing: border-box;
    border-radius: 36px;
    border: 6px solid var(--green-dark);
    background: linear-gradient(180deg, #a6d85a 0%, var(--green) 55%, #76b02c 100%);
    display: flex;
    align-items: center;
    justify-content: center;
    gap: 48px;
    font-size: 72px;
    font-weight: 700;
    color: var(--button-ink);
    text-decoration: none;
  }
  .banner__cta-arrow {
    width: 72px;
    height: 84px;
  }
</style>
</head>
<body>
<main class="banner">
  <svg class="banner__backdrop" viewBox="0 0 1200 2400" aria-hidden="true">
    <defs>
      <linearGradient id="orangeField" x1="0" y1="0" x2="1" y2="1">
        <stop offset="0" stop-color="#f9a53a"/>
        <stop offset="0.5" stop-color="#f7941d"/>
        <stop offset="1" stop-color="#f26f21"/>
      </linearGradient>
      <radialGradient id="glow" cx="0.8" cy="0.1" r="0.6">
        <stop offset="0" stop-color="#ffd89a" stop-opacity="0.8"/>
        <stop offset="1" stop-color="#ffd89a" stop-opacity="0"/>
      </radialGradient>
      <linearGradient id="lowerField" x1="0" y1="0" x2="0" y2="1">
        <stop offset="0" stop-color="#eceef0"/>
        <stop offset="1" stop-color="#ffffff"/>
      </linearGradient>
    </defs>
    <rect class="lower-field" x="0" y="0" width="1200" height="2400" fill="url(#lowerField)"/>
    <polygon class="green-stripe" points="0,1560 1200,660 1200,930 0,1680" fill="#8dc63f"/>
    <polygon class="orange-field" points="0,0 1200,0 1200,680 0,1580" fill="url(#orangeField)"/>
    <polygon class="orange-glow" points="0,0 1200,0 1200,680 0,1580" fill="url(#glow)"/>
  </svg>

  <div class="banner__portrait" role="img" aria-label="Photo of Brody Halvaney in a light grey suit jacket and dark shirt"></div>

  <h1 class="banner__name">Brody Halvaney</h1>
  <h2 class="banner__headline">
    <span class="banner__rank">#1</span>
    Real<br>Estate<br>Investing<br>Strategy
  </h2>

  <a class="banner__cta" href="#">
    GET STARTED
    <svg class="banner__cta-arrow" viewBox="0 0 72 84" aria-hidden="true">
      <polygon points="0,0 72,42 0,84" fill="#2f4a16"/>
    </svg>
  </a>
</main>
</body>
</html>
```